Business Card Design Project

business cards to match the logo design reference 1970674
specific details to be provided asap - message to follow
hello - thank you for the logo design (reference 1970674) which we are very happy with. In terms of business cards you presented a couple of options ie blue front/white back and then the reverse. Can we start with the white front version but change the text details to black font?
Actual details are as follows;
Dorian Plimsoll
Managing Director
e dorianplimsoll@kestrowe.com.au
t +61 2 5550 1937
m +61 400 555 219
Suite 712, Level 7, 48 Thornbury Rd
Sydney, NSW 2000, Australia
www.kestrowe.com.au

```html
<!DOCTYPE html>
<html lang="en">
<head>
<meta charset="utf-8">
<title>Kestrowe Business Card Options</title>
<link rel="stylesheet" href="https://fonts.googleapis.com/css2?family=Didact+Gothic&family=Open+Sans:wght@400&display=swap">
<style>
  :root {
    --backdrop: #d6d7d9;
    --card: #ffffff;
    --ink: #111111;
    --label-blue: #2b7cc2;
    --brand-blue: #7fb3e3;
  }
  * { margin: 0; padding: 0; box-sizing: border-box; }
  html, body {
    width: 1200px;
    height: 650px;
    overflow: hidden;
    background: var(--backdrop);
  }
  .presentation {
    position: relative;
    width: 1200px;
    height: 650px;
  }
  .card {
    position: absolute;
    top: 165px;
    width: 585px;
    height: 350px;
    background: var(--card);
    color: var(--ink);
    font-family: "Open Sans", sans-serif;
  }
  .card--option-a { left: 0; }
  .card--option-b { left: 615px; }

  .identity {
    position: absolute;
    left: 40px;
    top: 14px;
    font-family: "Didact Gothic", sans-serif;
    font-variant: small-caps;
    font-weight: 400;
    line-height: 1;
  }
  .card--option-a .identity__name {
    font-size: 62px;
    letter-spacing: 1px;
  }
  .card--option-a .identity__role {
    font-size: 24px;
    letter-spacing: 1px;
    margin-top: -4px;
    margin-left: 2px;
  }
  .card--option-b .identity { top: 26px; }
  .card--option-b .identity__name,
  .card--option-b .identity__role {
    font-size: 44px;
    letter-spacing: 1px;
    line-height: 0.98;
  }

  .contact {
    position: absolute;
    left: 44px;
    top: 150px;
    list-style: none;
    font-size: 16.5px;
    line-height: 25.5px;
  }
  .contact__label {
    display: inline-block;
    width: 28px;
    color: var(--label-blue);
  }
  .address {
    position: absolute;
    left: 43px;
    top: 269px;
    font-style: normal;
    font-size: 16px;
    line-height: 22.5px;
  }

  .brand {
    position: absolute;
    left: 400px;
    top: 152px;
    display: flex;
    align-items: center;
    gap: 10px;
    color: var(--brand-blue);
    font-family: "Open Sans", sans-serif;
    font-size: 26px;
    font-weight: 400;
  }
  .brand__dot {
    width: 18px;
    height: 18px;
    border-radius: 50%;
    background: var(--brand-blue);
  }
</style>
</head>
<body>
<main class="presentation">

  <section class="card card--option-a" aria-label="Business card option A">
    <header class="identity">
      <div class="identity__name">Dorian Plimsoll</div>
      <div class="identity__role">Managing Director</div>
    </header>
    <ul class="contact">
      <li><span class="contact__label">E</span>dorianplimsoll@kestrowe.com.au</li>
      <li><span class="contact__label">T</span>+61 2 5550 1937</li>
      <li><span class="contact__label">M</span>+61 400 555 219</li>
    </ul>
    <address class="address">
      Suite 712, Level 7, 48 Thornbury Rd<br>
      Sydney, NSW 2000, Australia
    </address>
    <div class="brand"><span class="brand__dot"></span>Kestrowe</div>
  </section>

  <section class="card card--option-b" aria-label="Business card option B">
    <header class="identity">
      <div class="identity__name">Dorian Plimsoll</div>
      <div class="identity__role">Managing Director</div>
    </header>
    <ul class="contact">
      <li><span class="contact__label">E</span>dorianplimsoll@kestrowe.com.au</li>
      <li><span class="contact__label">T</span>+61 2 5550 1937</li>
      <li><span class="contact__label">M</span>+61 400 555 219</li>
    </ul>
    <address class="address">
      Suite 712, Level 7, 48 Thornbury Rd<br>
      Sydney, NSW 2000, Australia
    </address>
    <div class="brand"><span class="brand__dot"></span>Kestrowe</div>
  </section>

</main>
</body>
</html>
```